Logo + Label Design (Men’s Grooming Brand & Product Packaging)

Design a logo and 2 oz pomade label for Brant, a modern men’s grooming brand focused on clean, high-quality, natural ingredients. The design should establish a bold, masculine, minimalist identity that can later extend to products like shaving gel and body wash.

Key Requirements

Create a primary logo for “Brant” and a core label for the 2 oz pomade jar (screw-top).

Use a clean, modern style — masculine, confident, and approachable (think Wendel’s, Valto, Northfield Mill).

Design for 1–2 color screen printing on solid jar colors (white, black, or navy).

Avoid gradients, foil, or embossing. Must work in black & white.

Provide: vector logo, mockup of the 2 oz jar, color palette (CMYK/RGB/HEX), and font specs.

Winning design may lead to future projects (body wash, shave gel, skincare lines).

Font styles to use
Other font styles liked:
• We like the fonts and design concept in the attached mockup.

Requirements
Should not have
• We want to avoid too much writing or busy designs. We want to avoid having graphics/illustrations embedded in the logo if they will cause the brand to look less classy or sophisticated. We also want the design to look simple and all-American (e.g. Pellham and Stroud, Tall Pine, The BRIM, etc). We’d like to give a Kessler & Dunmore vibe that feels classy and high end.

```html
<!DOCTYPE html>
<html lang="en">
<head>
<meta charset="utf-8">
<title>Brant Hair Pomade – Label</title>
<link rel="stylesheet" href="https://fonts.googleapis.com/css2?family=Montserrat:wght@500;600;700;800&family=Oswald:wght@500&display=swap">
<style>
  :root {
    --ink: #111111;
    --paper: #ffffff;
    --label-white: #f2f2f2;
    --rule: #d4d4d4;
  }
  * { margin: 0; padding: 0; box-sizing: border-box; }
  html, body { width: 1200px; height: 778px; overflow: hidden; background: var(--paper); }
  .canvas { position: relative; width: 1200px; height: 778px; background: var(--paper); font-family: "Montserrat", sans-serif; }

  /* Side wrap label, shown flat */
  .side-label {
    position: absolute; left: 150px; top: 320px; width: 580px; height: 170px;
    background: var(--label-white); border: 1px solid var(--rule);
  }
  .side-label__band {
    position: absolute; left: 0; top: 26px; width: 100%; height: 56px;
    background: var(--ink); color: var(--paper);
    display: flex; align-items: center; justify-content: center;
    font-weight: 600; font-size: 20px; letter-spacing: 0.42em; padding-left: 0.42em;
  }
  .side-label__info {
    position: absolute; left: 0; top: 82px; width: 100%; height: 88px;
    display: flex; align-items: center; justify-content: space-between; padding: 0 28px;
    color: var(--ink);
  }
  .brand-mark { font-weight: 800; font-size: 26px; letter-spacing: 0.02em; color: var(--ink); }
  .product-variant { display: flex; flex-direction: column; align-items: center; gap: 4px; }
  .product-variant__name { font-weight: 700; font-size: 18px; letter-spacing: 0.08em; }
  .product-variant__tag {
    background: var(--ink); color: var(--paper);
    font-weight: 600; font-size: 8.5px; letter-spacing: 0.04em; padding: 3px 6px;
  }
  .net-weight { font-family: "Oswald", sans-serif; font-weight: 500; font-size: 13px; }

  /* Lid label */
  .lid-label {
    position: absolute; left: 800px; top: 303px; width: 228px; height: 228px;
    border-radius: 50%; background: var(--ink); color: var(--paper);
    display: flex; flex-direction: column; align-items: center; text-align: center;
    padding-top: 44px;
  }
  .lid-label .brand-mark { color: var(--paper); font-size: 22px; }
  .lid-label__title { margin-top: 20px; font-weight: 600; font-size: 17px; line-height: 1.05; letter-spacing: 0.03em; }
  .lid-label__variant { margin-top: 12px; font-weight: 700; font-size: 9px; letter-spacing: 0.14em; }
  .lid-label__tag {
    margin-top: 4px; background: var(--paper); color: var(--ink);
    font-weight: 600; font-size: 5.5px; letter-spacing: 0.03em; padding: 2px 4px;
  }
  .lid-label .net-weight { margin-top: 24px; font-size: 8px; }
</style>
</head>
<body>
<main class="canvas">
  <section class="side-label" aria-label="Jar side label">
    <div class="side-label__band">HAIR POMADE</div>
    <div class="side-label__info">
      <span class="brand-mark">BRANT</span>
      <div class="product-variant">
        <span class="product-variant__name">FRESH &amp; CLEAN</span>
        <span class="product-variant__tag">MEDIUM HOLD – MATTE FINISH</span>
      </div>
      <span class="net-weight">NET WT 2 OZ (57 G)</span>
    </div>
  </section>

  <section class="lid-label" aria-label="Jar lid label">
    <span class="brand-mark">BRANT</span>
    <h1 class="lid-label__title">HAIR<br>POMADE</h1>
    <span class="lid-label__variant">FRESH &amp; CLEAN</span>
    <span class="lid-label__tag">MEDIUM HOLD – MATTE FINISH</span>
    <span class="net-weight">NET WT 2 OZ (57 G)</span>
  </section>
</main>
</body>
</html>
```